Broschüre für Nachlassverwaltung und Testamentsvollstreckung
Zielgruppe
Nachlassverwaltung und Testamentsvollstreckung
Aufgabenstellung
Ich brauche:
1. ) Präsentationsmappe: mit Visitenkartentasche innenliegend links unten, Endformat: 440 x 307 mm
Endformat: 440 x 307 mm
Seitenanzahl: 2-seitig
Farbigkeit: 4/4-farbig
Diese Beschreibung bezieht sich auf unsere Topseller-Sorte 0,40 mm starker Chromokarton 255g (zertifiziert mit GWNA-Siegel für Nachhaltigkeit), hohe Steifigkeit mit 1,6-fachem Volumen. Weitere Sorten finden Sie in der Produktauswahl.
Hochwertige Mappe für DIN A4, 4/4 farbig (Außen- und Innenseite bedruckt)
0,40 mm starker Chromokarton 255g (zertifiziert mit GWNA-Siegel für Nachhaltigkeit), hohe Steifigkeit mit 1,6-fachem Volumen
Datenformat: 45,0 x 31,7 cm
Endformat: 44,0 x 30,7 cm
2. ) Ringordner
Ringbuch (2-Loch) bis zu 400 DIN A4 Blätter
Außen- und Innenseite farbig bedruckt (4/4)
Hochwertiger Qualitätsdruck mit Glanzfolie veredelt
4/4 farbig außen und innen
Endformat: 61,5 cm x 31,5 cm
geschlossenes Endformat: 28,2 cm x 31,5 cm
Datenformat: 65,1 cm x 35,1 cm
Folgende Dienstleistungen sollten mit aufgeführt sein:
- Testamentsvollstreckung
- Nachlassabwicklung
- Nachlassverwaltung
- Nachlasspflege

```html
<!DOCTYPE html>
<html lang="de">
<head>
<meta charset="utf-8">
<title>Erbwerk Nachlassmanagement – Präsentationsmappe</title>
<link rel="stylesheet" href="https://fonts.googleapis.com/css2?family=Playfair+Display:wght@700&family=Questrial&display=swap">
<style>
  :root {
    --bg: #d4d4d4;
    --cream: #f7f2eb;
    --taupe: #a39c90;
    --text: #2f2d2a;
    --muted: #9b9892;
    --band: #1d1c1b;
    --band-text: #e9e4dc;
    --teal-dark: #1f3336;
    --mark-fill: #d8d2c8;
    --mark-dark: #8f897f;
  }
  * { margin: 0; padding: 0; box-sizing: border-box; }
  html, body { width: 1200px; height: 1200px; overflow: hidden; }
  body {
    background: var(--bg);
    font-family: "Questrial", "Century Gothic", sans-serif;
    color: var(--text);
    position: relative;
  }
  .spread {
    position: absolute;
    left: 200px;
    width: 800px;
    height: 558px;
    box-shadow: 0 6px 18px rgba(0,0,0,.25);
    overflow: hidden;
  }
  .spread--outside { top: 28px; }
  .spread--inside { top: 614px; }
  .page { position: absolute; top: 0; width: 400px; height: 558px; }
  .page--left { left: 0; }
  .page--right { left: 400px; }

  .band {
    position: absolute; left: 0; right: 0; bottom: 0; height: 43px;
    background: var(--band);
    display: flex; align-items: center; justify-content: center;
  }
  .wordmark {
    font-family: "Questrial", "Century Gothic", sans-serif;
    font-size: 10px;
    letter-spacing: .3px;
    white-space: nowrap;
  }
  .band .wordmark { color: var(--band-text); }
  .footer-mark {
    position: absolute; bottom: 22px; left: 0; right: 0;
    text-align: center;
  }
  .footer-mark .wordmark { color: #55524d; }

  .back { background: var(--cream); }
  .back__photo {
    position: absolute; left: 0; top: 0; width: 400px; height: 200px;
    background: linear-gradient(180deg, #e6ddd0 0%, #eee7dd 55%, var(--cream) 100%);
  }
  .services { position: absolute; left: 60px; top: 218px; list-style: none; }
  .services li {
    font-family: "Playfair Display", serif;
    font-weight: 700;
    font-size: 15px;
    line-height: 39px;
  }
  .services li::before { content: "• "; }
  .services .is-dark { color: var(--text); }
  .services .is-light { color: var(--muted); }
  .contact {
    position: absolute; left: 60px; top: 398px;
    font-size: 8.5px; line-height: 11px; color: var(--text);
  }
  .contact p + p { margin-top: 9px; }
  .badge {
    position: absolute; left: 309px; top: 449px; width: 73px; height: 90px;
    background: #f4f1ea; border: 3px solid #c9b98a; border-radius: 8px;
    box-shadow: 0 2px 6px rgba(0,0,0,.35); z-index: 2;
  }

  .front__photo {
    position: absolute; inset: 0 0 43px 0;
    background: linear-gradient(180deg, #f4efe6 0%, #ece4d7 40%, #c9c7bd 58%, #4e6466 72%, var(--teal-dark) 100%);
  }

  .inner-left { background: var(--cream); }
  .inner-right { background: linear-gradient(90deg, #ece6dc 0%, #c9c2b6 55%, var(--taupe) 100%); }
  .portrait {
    position: absolute; left: 45px; top: 45px; width: 130px; height: 181px;
    border-radius: 9px;
    background: linear-gradient(180deg, #d9d6d1 0%, #8c8883 60%, #3b3a38 100%);
  }
  .person {
    position: absolute; left: 45px; top: 236px; width: 130px; text-align: center;
    font-family: "Playfair Display", serif; font-weight: 700; font-size: 12.5px; color: var(--text);
  }
  .copy { position: absolute; font-size: 7.6px; line-height: 9.3px; color: var(--text); }
  .copy p + p { margin-top: 9px; }
  .copy--intro { left: 49px; top: 286px; width: 130px; }
  .copy--main { left: 205px; top: 45px; width: 172px; }

  .memberships { position: absolute; left: 205px; top: 400px; width: 175px; }
  .member-mark { background: var(--mark-fill); }
  .member-mark--wide { width: 76px; height: 14px; border-radius: 2px; }
  .member-row { display: flex; align-items: center; gap: 24px; margin-top: 14px; }
  .member-mark--round { width: 38px; height: 38px; border-radius: 50%; }
  .member-mark--block { width: 78px; height: 24px; background: var(--mark-dark); }
</style>
</head>
<body>

<section class="spread spread--outside" aria-label="Mappe Außenseite">
  <div class="page page--left back">
    <div class="back__photo" role="img" aria-label="Blasses Foto: Schreibtisch mit Richterhammer, Waage und Akten"></div>
    <ul class="services">
      <li class="is-dark">Testamentsvollstreckung</li>
      <li class="is-light">Nachlassabwicklung</li>
      <li class="is-dark">Nachlassverwaltung</li>
      <li class="is-light">Nachlasspflege</li>
    </ul>
    <div class="contact">
      <p>Nachlassmanagement<br>Marlene Hollweg</p>
      <p>Lindenallee 7<br>48301 Nordhagen</p>
      <p>Mail: info@erbwerk-nachlass.de</p>
      <p>Tel.: +49 (0) 2501 / 44 20 310<br>Fax: +49 (0) 2501 / 44 20 311</p>
    </div>
    <div class="badge" aria-hidden="true"></div>
    <div class="band"><span class="wordmark">Erbwerk Nachlassmanagement</span></div>
  </div>
  <div class="page page--right">
    <div class="front__photo" role="img" aria-label="Foto: Mann im Anzug steigt eine lange Treppe hinauf ins Licht"></div>
    <div class="band"><span class="wordmark">Erbwerk Nachlassmanagement</span></div>
  </div>
</section>

<section class="spread spread--inside" aria-label="Mappe Innenseite">
  <div class="page page--left inner-left">
    <div class="portrait" role="img" aria-label="Schwarzweiß-Porträtfoto der Inhaberin"></div>
    <p class="person">Marlene Hollweg</p>
    <div class="copy copy--intro">
      <p>Ich bin seit 35 Jahren Unternehmerin und habe davon 22 Jahre lang für meine damaligen Auftraggeber, zu denen unter anderem Angehörige oder Nachlasskanzleien zählten, Werte gesichert und Erbenrecherchen durchgeführt.</p>
    </div>
    <div class="copy copy--main">
      <p>Bis heute widme ich mich mit der gleichen Leidenschaft, Hingabe und vor allem mit viel Herz der Testamentsvollstreckung und Nachlassabwicklung.</p>
      <p>Ich bin eine geprüfte und zertifizierte Testamentsvollstreckerin sowie eine geprüfte und zertifizierte Nachlasspflegerin. Durch meine aktive Mitgliedschaft im BNP (Bundesverband Nachlasspflege), der VEVN (Vereinigung für Erbrecht und Vermögensnachfolge e.V.) und dem ATV (Arbeitskreis Testamentsvollstreckung und Vorsorge e.V.) halte ich mich jährlich durch fachspezifische Lehrgänge und Veranstaltungen auf dem neuesten Stand der Rechtsprechung im Erb- und Nachlassrecht.</p>
      <p>In den letzten Jahren habe ich ein Netzwerk aus Steuerberatern, Rechtsanwälten, Notaren sowie Maklern und weiteren Dienstleistern aufgebaut, um Ihnen eine schnelle und sorgenfreie Abwicklung anbieten zu können.</p>
      <p>Gerne übernehme ich beruflich die Nachlassabwicklung oder Testamentsvollstreckung für gemeinnützige Organisationen oder Privatpersonen.</p>
      <p>Ich würde mich freuen, Sie begleiten zu dürfen!</p>
    </div>
    <div class="memberships" role="img" aria-label="Platz für Zeichen der Mitgliedsverbände">
      <div class="member-mark member-mark--wide"></div>
      <div class="member-row">
        <div class="member-mark member-mark--round"></div>
        <div class="member-mark member-mark--block"></div>
      </div>
    </div>
    <div class="footer-mark"><span class="wordmark">Erbwerk Nachlassmanagement</span></div>
  </div>
  <div class="page page--right inner-right">
    <div class="footer-mark"><span class="wordmark">Erbwerk Nachlassmanagement</span></div>
  </div>
</section>

</body>
</html>
```